Veranta - Solution provider in business consulting

Veranta is a swiss based company providing solutions for developing markets. The business covers various fields of business consulting, such as supply chain, product costs, quality management and manufacturing management. The Business operates in a efficient, straight and solution oriented manner.
The final design should communicate these characteristics. Asian people as well as as western people shall identify the qualities of the company at first sight.
The customer needs business cards with a simple view but an recognizable design, printed in high quality. Engraved elements such as the globe or simple words are possible.
Available colors are: (RAL)
102/102/102
51/102/102
153/204/153
255/102/51
Font: Calibri
Industry/Entity Type
Business
Look and feel
Each slider illustrates characteristics of the customer's brand and the style your logo design should communicate.

```html
<!DOCTYPE html>
<html lang="en">
<head>
<meta charset="utf-8">
<title>Veranta business card</title>
<link rel="stylesheet" href="https://fonts.googleapis.com/css2?family=Carlito:wght@400;700&display=swap">
<style>
  :root {
    --bg: #e6e6e4;
    --card-dark: #1b1b1b;
    --card-light: #fafafa;
    --mark-grey: #666666;
    --text: #333333;
    --text-soft: #555555;
  }
  * { margin: 0; padding: 0; box-sizing: border-box; }
  html, body { width: 1200px; height: 1021px; overflow: hidden; }
  body {
    background: var(--bg);
    font-family: "Carlito", "Calibri", sans-serif;
    position: relative;
  }
  .card {
    position: absolute;
    top: 342px;
    width: 520px;
    height: 336px;
    border-radius: 3px;
    box-shadow: 0 2px 10px rgba(0,0,0,0.12);
  }
  .card-back { left: 50px; background: var(--card-dark); }
  .card-front { left: 630px; background: var(--card-light); }

  .back-name {
    position: absolute;
    left: 50%; top: 50%;
    transform: translate(-50%, -50%);
    display: flex; align-items: center; gap: 14px;
    color: var(--mark-grey);
    font-size: 48px;
    letter-spacing: 1px;
  }
  .mark-dot {
    width: 36px; height: 36px; border-radius: 50%;
    background: var(--mark-grey);
  }

  .front-name {
    position: absolute;
    left: 36px; top: 190px;
    display: flex; align-items: center; gap: 8px;
    color: var(--mark-grey);
    font-size: 36px;
    letter-spacing: 0.5px;
  }
  .front-name .mark-dot { width: 22px; height: 22px; }

  .contact {
    position: absolute;
    left: 292px; top: 44px;
    color: var(--text-soft);
    font-size: 14px;
    line-height: 18px;
  }
  .person { color: var(--text); font-weight: 700; font-size: 17px; line-height: 20px; }
  .role { margin-bottom: 2px; }
  .row { display: flex; align-items: flex-start; gap: 8px; }
  .row + .row { margin-top: 4px; }
  .address { margin-bottom: 6px; }
  .icon { width: 11px; height: 11px; margin-top: 3px; flex: none; fill: var(--text-soft); }
</style>
</head>
<body>
  <section class="card card-back" aria-label="Card back">
    <div class="back-name"><span class="mark-dot"></span><span>veranta</span></div>
  </section>

  <section class="card card-front" aria-label="Card front">
    <div class="front-name"><span>veranta</span><span class="mark-dot"></span></div>

    <div class="contact">
      <div class="person">Marco Ellin</div>
      <div class="role">CEO</div>
      <div class="row address">
        <svg class="icon" viewBox="0 0 12 12"><path d="M6 0a4 4 0 0 0-4 4c0 3 4 8 4 8s4-5 4-8a4 4 0 0 0-4-4zm0 5.6A1.6 1.6 0 1 1 6 2.4a1.6 1.6 0 0 1 0 3.2z"/></svg>
        <div>Veranta GmbH<br>Feldweg 14<br>9200 Talbach<br>Switzerland</div>
      </div>
      <div class="row">
        <svg class="icon" viewBox="0 0 12 12"><path d="M3 0h6a1 1 0 0 1 1 1v10a1 1 0 0 1-1 1H3a1 1 0 0 1-1-1V1a1 1 0 0 1 1-1zm0 1.5v8h6v-8z"/></svg>
        <div>+41 79 000 1234</div>
      </div>
      <div class="row">
        <svg class="icon" viewBox="0 0 12 12"><path d="M1 3c2-2 8-2 10 0l-1 2-2-.5V3.5H4v1L2 5zM2 6h8l1 5H1z"/></svg>
        <div>+41 71 000 5678</div>
      </div>
      <div class="row">
        <svg class="icon" viewBox="0 0 12 12"><path d="M0 2h12v8H0zm1 1v.4l5 3.2 5-3.2V3z"/></svg>
        <div>marco.ellin@veranta.ch</div>
      </div>
      <div class="row">
        <svg class="icon" viewBox="0 0 12 12"><circle cx="6" cy="6" r="5.5"/><path d="M0.5 6h11M6 .5v11" stroke="#fafafa" stroke-width="0.8"/></svg>
        <div>www.veranta.ch</div>
      </div>
    </div>
  </section>
</body>
</html>
```